Lumo Pharma Chinese Traditional Medicine Web Design

We need a web design for a new company based in Shanghai China called 'Lumo Pharma'. We develop Chinese traditional herbal medicine, including research and development, technical support service, manufacturing, . Also, there’s a small ratio of western medicine. Our goal is to contributing to a healthier future.

Target Market(s)

global,but mainly China

Industry/Entity Type

Pharmaceutical

Number of Pages Required

1 page

Font styles to use
Serif

Colors
e4daeb
cedeed
cadf82
eaf2ce
fbd4d5
fee3d4
fabb94
fee18a
b8a6cd

Requirements
Must have
• triditional Chinese elements, concept of herbal, health, value, better life for people..could be colourful but not more than 3 different colour..
Nice to have
• Style: simple, communicate traditional Chinese herbal medicine element, as well as modern technique..same as LOGO style..
Should not have
• please dont show more IT elements...

```html
<!DOCTYPE html>
<html lang="zh">
<head>
<meta charset="utf-8">
<title>璐墨医药 Lumo Pharma</title>
<link href="https://fonts.googleapis.com/css2?family=Noto+Sans+SC:wght@400;500;700&family=Noto+Serif+SC:wght@500&family=Open+Sans:wght@400;700&display=swap" rel="stylesheet">
<style>
:root{
  --brown:#7a4a2e;
  --brown-dark:#6b3f26;
  --sage:#5f6b5a;
  --grey-bg:#e8e9ec;
  --text:#6a5a50;
  --white:#ffffff;
}
*{margin:0;padding:0;box-sizing:border-box}
html,body{width:1200px;height:3538px;overflow:hidden}
body{position:relative;background:var(--white);font-family:"Noto Sans SC",sans-serif;color:var(--text)}
.abs{position:absolute}
.brand{display:flex;align-items:center;gap:12px}
.brand-dot{width:44px;height:44px;border-radius:50%;background:var(--brown)}
.brand-name{font-family:"Noto Serif SC",serif;font-weight:500;font-size:20px;color:var(--brown);line-height:1.2}
.header-contact{font-family:"Open Sans",sans-serif;font-size:13px;color:var(--brown);font-weight:700;line-height:1.3}
.social{display:flex;gap:6px}
.social span{width:20px;height:20px;border-radius:50%;background:var(--sage)}
.nav{top:128px;left:0;width:1200px;height:39px;background:var(--brown)}
.nav a{position:absolute;top:0;height:39px;width:136px;margin-left:-68px;text-align:center;line-height:39px;color:var(--white);font-size:22px;text-decoration:none}
.nav a.active{background:var(--sage)}
.hero{top:167px;left:0;width:1200px;height:533px;background:
  radial-gradient(ellipse 260px 160px at 560px 420px,#d9b58a 0%,rgba(217,181,138,0) 100%),
  radial-gradient(ellipse 220px 170px at 1020px 420px,#8c7a4e 0%,rgba(140,122,78,0) 100%),
  radial-gradient(ellipse 240px 140px at 260px 110px,#6a2a22 0%,rgba(106,42,34,0) 100%),
  radial-gradient(ellipse 200px 140px at 830px 80px,#c9c2b4 0%,rgba(201,194,180,0) 100%),
  linear-gradient(180deg,#4a372c 0%,#6e5646 38%,#c9bba6 62%,#a99582 100%)}
.hero h1{position:absolute;top:212px;width:100%;text-align:center;color:var(--white);font-size:52px;font-weight:700;line-height:64px;text-shadow:0 2px 6px rgba(0,0,0,.5)}
.hero .arrow{position:absolute;top:240px}
.dots{position:absolute;top:482px;left:469px;display:flex;gap:14px}
.dots span{width:14px;height:14px;border-radius:50%;background:var(--brown)}
.dots span.on{background:var(--white)}
.welcome-photo{top:700px;left:550px;width:650px;height:485px;background:
  radial-gradient(ellipse 170px 260px at 420px 300px,#f2f0ec 0%,#e4e0da 55%,rgba(228,224,218,0) 100%),
  radial-gradient(ellipse 120px 110px at 430px 150px,#c89a76 0%,rgba(200,154,118,0) 100%),
  linear-gradient(90deg,#ffffff 0%,#efe6d8 18%,#d8c2a0 40%,#c9ad84 70%,#b89a72 100%)}
.welcome h2{font-size:32px;font-weight:500;color:var(--brown);line-height:40px}
.body-text{font-size:15px;line-height:20px;color:var(--text)}
.btn{background:var(--brown);color:var(--white);font-size:15px;font-weight:700;text-align:center;border-radius:3px}
.products{top:1185px;left:0;width:1200px;height:1018px;background:var(--grey-bg)}
.section-title{display:flex;align-items:center;gap:14px;font-size:38px;font-weight:500;color:var(--brown)}
.section-title i{display:block;width:40px;height:40px;border-radius:50%;background:var(--sage)}
.card{width:296px;height:284px;border:1px solid #b8b0a8;background:#fff}
.card-label{width:296px;text-align:center;font-size:15px;color:var(--brown)}
.newsletter{top:2203px;left:0;width:1200px;height:337px;background:
  radial-gradient(ellipse 300px 200px at 520px 90px,#a9a99a 0%,rgba(169,169,154,0) 100%),
  radial-gradient(ellipse 260px 180px at 1050px 120px,#7a5636 0%,rgba(122,86,54,0) 100%),
  linear-gradient(120deg,#77755c,#8e8c6c 45%,#6e6450)}
.news-img{width:258px;height:174px}
.news-cap{font-size:14px;color:var(--text)}
.news-date{font-family:"Open Sans",sans-serif;font-size:12px;color:var(--text)}
.footer{top:3101px;left:0;width:1200px;height:371px;background:var(--brown)}
.footer h3{font-size:19px;font-weight:500;color:var(--white)}
.footer ul{list-style:none}
.footer li{font-size:14px;color:var(--white);line-height:27px}
.footer li::before{content:"›";margin-right:12px}
.copyright{top:3472px;left:0;width:1200px;height:66px;background:var(--sage);color:var(--white);font-family:"Open Sans",sans-serif;font-size:13px;font-weight:700;text-align:center;line-height:66px}
</style>
</head>
<body>

<header>
  <div class="abs brand" style="top:40px;left:113px">
    <span class="brand-dot"></span>
    <span class="brand-name">Lumo Pharma</span>
  </div>
  <div class="abs" style="top:52px;left:798px;display:flex;gap:8px;align-items:center">
    <svg width="22" height="26" viewBox="0 0 24 24"><path d="M6.6 10.8c1.4 2.8 3.8 5.1 6.6 6.6l2.2-2.2c.3-.3.7-.4 1-.2 1.1.4 2.3.6 3.6.6.6 0 1 .4 1 1V20c0 .6-.4 1-1 1C10.6 21 3 13.4 3 4c0-.6.4-1 1-1h3.5c.6 0 1 .4 1 1 0 1.3.2 2.5.6 3.6.1.3 0 .7-.2 1z" fill="#7a4a2e"/></svg>
    <div class="header-contact">Call Us<br>555-210-4836</div>
  </div>
  <div class="abs" style="top:44px;left:1003px">
    <div class="header-contact" style="text-align:center;margin-bottom:3px">Visit us</div>
    <div class="social"><span></span><span></span><span></span><span></span></div>
  </div>
</header>

<nav class="abs nav">
  <a href="#" class="active" style="left:180px">公司首页</a>
  <a href="#" style="left:343px">公司概况</a>
  <a href="#" style="left:505px">新闻中心</a>
  <a href="#" style="left:669px">产品服务</a>
  <a href="#" style="left:832px">职业发展</a>
  <a href="#" style="left:995px">联系我们</a>
</nav>

<section class="abs hero" role="img" aria-label="Chinese herbal ingredients, mortar and calligraphy paper on a wooden table">
  <h1>個兩把、備我一市有方懷需成沒<br>起動於係本出告會我公卻</h1>
  <svg class="arrow" style="left:40px" width="30" height="54" viewBox="0 0 30 54"><path d="M26 3 4 27l22 24" stroke="#fff" stroke-width="3" fill="none"/></svg>
  <svg class="arrow" style="left:1130px" width="30" height="54" viewBox="0 0 30 54"><path d="M4 3l22 24L4 51" stroke="#fff" stroke-width="3" fill="none"/></svg>
  <div class="dots"><span class="on"></span><span></span><span></span><span></span><span></span></div>
</section>

<section class="welcome">
  <div class="abs welcome-photo" role="img" aria-label="Smiling pharmacist in a white coat beside stacked paper herb packages"></div>
  <div class="abs" style="top:765px;left:100px;display:flex;gap:14px">
    <i style="display:block;width:40px;height:40px;border-radius:50%;background:var(--sage);margin-top:28px"></i>
    <h2 style="margin-top:28px">欢迎来到<br>璐墨医药（上海）有限公司</h2>
  </div>
  <p class="abs body-text" style="top:914px;left:113px;width:530px">璐墨医药（上海）有限公司 是一家製藥公司，於2019年在中國上海註冊，致力於研發中草藥，包括研發，技術支持服務，製造以及頂級專家團隊。 而且，西醫的比例很小。</p>
  <p class="abs body-text" style="top:994px;left:113px;width:530px">中醫的特點是，它不僅可以治癒疾病，而且可以使人們遠離疾病，具有數千年的實踐經驗。 我們的目標是為更健康的未來做出貢獻。</p>
  <div class="abs btn" style="top:1082px;left:113px;width:117px;height:40px;line-height:40px">更多信息</div>
</section>

<section class="abs products">
  <div class="abs section-title" style="top:90px;left:470px"><i></i>产品服务</div>
  <p class="abs body-text" style="top:173px;left:138px;font-size:13px;line-height:30px;width:930px">個兩把、備我一市有方懷需成沒起動於係本出告會我公卻，料高語我語老小，檢再假黑那，就友吃沒足都的價有的，心勢出麼站林以。<br>一是高如這山裡：發一一度你，出待現帶當共說好，作不獨家音續小：這盤選計重的年他來現不安！把藝的了工來，很界元語資字同後</p>

  <div class="abs card" style="top:268px;left:124px;background:radial-gradient(ellipse 110px 70px at 110px 130px,#2e2a28 0%,#5a4a3c 40%,#c99a62 70%,rgba(201,154,98,0) 100%),radial-gradient(ellipse 30px 90px at 230px 150px,#c98a3a 0%,rgba(201,138,58,0) 100%),#ffffff" role="img" aria-label="Black herbal powder in a wooden bowl with an oil bottle"></div>
  <div class="abs card" style="top:268px;left:446px;background:radial-gradient(ellipse 100px 60px at 115px 110px,#b7ad4a 0%,#b56a3e 55%,rgba(181,106,62,0) 100%),radial-gradient(ellipse 70px 60px at 230px 170px,#3f7a2e 0%,rgba(63,122,46,0) 100%),#ffffff" role="img" aria-label="Green herbal powder in a clay bowl with fresh leaves"></div>
  <div class="abs card" style="top:268px;left:767px;background:radial-gradient(ellipse 130px 45px at 150px 175px,#b89066 0%,#d6c3a4 45%,rgba(214,195,164,0) 100%),radial-gradient(ellipse 50px 35px at 90px 160px,#4a3a30 0%,rgba(74,58,48,0) 100%),radial-gradient(ellipse 40px 30px at 250px 175px,#a83a2a 0%,rgba(168,58,42,0) 100%),#ffffff" role="img" aria-label="Dried herbs, roots and goji berries beside a white mortar"></div>
  <div class="abs card-label" style="top:562px;left:124px">产品1</div>
  <div class="abs card-label" style="top:562px;left:446px">产品2</div>
  <div class="abs card-label" style="top:562px;left:767px">产品3</div>

  <div class="abs card" style="top:610px;left:124px;background:radial-gradient(ellipse 90px 80px at 190px 170px,#c98a4a 0%,rgba(201,138,74,0) 100%),linear-gradient(135deg,#6e4a44,#a98577 55%,#c9b3a8)" role="img" aria-label="Herbal tea in a glass cup with lavender and a mortar"></div>
  <div class="abs card" style="top:610px;left:446px;background:radial-gradient(ellipse 60px 60px at 90px 130px,#e0902a 0%,rgba(224,144,42,0) 100%),radial-gradient(ellipse 50px 60px at 210px 100px,#9a5a3a 0%,rgba(154,90,58,0) 100%),radial-gradient(ellipse 40px 30px at 70px 230px,#c8302a 0%,rgba(200,48,42,0) 100%),#f1ede8" role="img" aria-label="Wooden spoons holding spices, chillies and cinnamon"></div>
  <div class="abs card" style="top:610px;left:767px;background:radial-gradient(ellipse 80px 50px at 110px 200px,#b48a68 0%,rgba(180,138,104,0) 100%),radial-gradient(ellipse 70px 70px at 240px 110px,#4e5a52 0%,rgba(78,90,82,0) 100%),linear-gradient(135deg,#e4e7ea,#d6d4cf)" role="img" aria-label="Herbal powder in a bowl with a stone mortar and pestle"></div>
  <div class="abs card-label" style="top:903px;left:124px">产品4</div>
  <div class="abs card-label" style="top:903px;left:446px">产品5</div>
  <div class="abs card-label" style="top:903px;left:767px">产品6</div>
</section>

<section class="abs newsletter" role="img" aria-label="Dried herbs and a mortar, softly darkened">
  <div class="abs section-title" style="top:60px;left:502px;color:var(--white)"><i style="background:var(--white)"></i>通讯</div>
  <div class="abs" style="top:218px;left:113px;font-size:32px;color:var(--white)">您的电子邮件在这里</div>
  <div class="abs" style="top:218px;left:432px;width:456px;height:38px;background:#e9e9e9"></div>
  <div class="abs btn" style="top:218px;left:903px;width:116px;height:40px;line-height:40px;background:#ececec;color:var(--brown)">更多信息</div>
</section>

<section class="news">
  <div class="abs section-title" style="top:2620px;left:478px"><i></i>新闻中心</div>
  <div class="abs news-img" style="top:2754px;left:139px;background:radial-gradient(ellipse 60px 50px at 200px 110px,#b9a06a 0%,rgba(185,160,106,0) 100%),linear-gradient(135deg,#2f2b24,#5c4e38 50%,#8a7452)" role="img" aria-label="Hands preparing herbs with small bottles and jars"></div>
  <div class="abs news-img" style="top:2754px;left:460px;background:radial-gradient(ellipse 80px 40px at 130px 150px,#8a7a6a 0%,rgba(138,122,106,0) 100%),linear-gradient(135deg,#e0e2e4,#bcb8b2,#ecebe8)" role="img" aria-label="Pharmacist grinding herbs in a laboratory"></div>
  <div class="abs news-img" style="top:2754px;left:780px;background:linear-gradient(180deg,#d8d6d2 0%,#c9a25a 30%,#e6ddcc 50%,#c79a4a 75%,#5a4a3a 100%)" role="img" aria-label="Shelves of herbal medicine jars"></div>
  <p class="abs news-cap" style="top:2952px;left:139px">備我一市有方懷需成沒起動於係本出告</p>
  <p class="abs news-date" style="top:2977px;left:139px">April 26, 2020</p>
  <p class="abs news-cap" style="top:2952px;left:460px">料高語我語老小 集修觀快樣理</p>
  <p class="abs news-date" style="top:2977px;left:460px">April 29, 2020</p>
  <p class="abs news-cap" style="top:2952px;left:780px">用院德我家工廣倒愛得我兒夜力</p>
  <p class="abs news-date" style="top:2977px;left:780px">April 30, 2020</p>
</section>

<footer class="abs footer">
  <div class="abs brand" style="top:70px;left:144px">
    <span class="brand-dot" style="background:var(--white)"></span>
    <span class="brand-name" style="color:var(--white)">Lumo Pharma</span>
  </div>
  <p class="abs" style="top:183px;left:150px;width:228px;font-size:15px;line-height:20px;color:var(--white)">璐墨医药（上海）有限公司 是一家製藥公司，於2019年在中國上海註冊，致力於研發中草藥，包括研發</p>
  <div class="abs social" style="top:288px;left:142px;gap:12px"><span style="background:#fff;width:24px;height:24px"></span><span style="background:#fff;width:24px;height:24px"></span><span style="background:#fff;width:24px;height:24px"></span><span style="background:#fff;width:24px;height:24px"></span></div>

  <h3 class="abs" style="top:80px;left:430px">快捷链接</h3>
  <ul class="abs" style="top:116px;left:433px">
    <li>公司首页</li><li>新闻中心</li><li>产品服务</li><li>职业发展</li><li>联系我们</li>
  </ul>

  <h3 class="abs" style="top:78px;left:587px">其他机构</h3>
  <ul class="abs" style="top:116px;left:588px">
    <li>华东草本产业联合会</li><li>本草质量评审中心</li><li>传统医药发展协会</li><li>草本健康贸易商会</li><li>青禾药材协会</li><li>东方草本研究院</li><li>药用植物应用研究所</li>
  </ul>

  <h3 class="abs" style="top:76px;left:884px;font-size:17px">联系我们</h3>
  <div class="abs" style="top:106px;left:886px;font-size:14px;line-height:26px;color:var(--white)">
    <div style="display:flex;gap:8px;align-items:flex-start"><svg width="14" height="20" viewBox="0 0 14 20" style="margin-top:4px"><path d="M7 1a6 6 0 0 0-6 6c0 4.5 6 12 6 12s6-7.5 6-12a6 6 0 0 0-6-6z" stroke="#fff" fill="none" stroke-width="1.5"/><circle cx="7" cy="7" r="2" fill="#fff"/></svg><span>璐墨医药（上海）有限公司<br>自由贸易试验区云杉路128号</span></div>
    <div style="display:flex;gap:8px;align-items:center"><svg width="14" height="14" viewBox="0 0 24 24"><path d="M6.6 10.8c1.4 2.8 3.8 5.1 6.6 6.6l2.2-2.2c.3-.3.7-.4 1-.2 1.1.4 2.3.6 3.6.6.6 0 1 .4 1 1V20c0 .6-.4 1-1 1C10.6 21 3 13.4 3 4c0-.6.4-1 1-1h3.5c.6 0 1 .4 1 1 0 1.3.2 2.5.6 3.6.1.3 0 .7-.2 1z" stroke="#fff" fill="none" stroke-width="2"/></svg>555-318-2047</div>
    <div style="display:flex;gap:8px;align-items:center"><svg width="14" height="12" viewBox="0 0 14 12"><rect x="1" y="1" width="12" height="10" stroke="#fff" fill="none" stroke-width="1.3"/><path d="M1 1l6 5 6-5" stroke="#fff" fill="none" stroke-width="1.3"/></svg>info@lumopharma</div>
    <div style="font-size:13px">网站备案 00000000000000号</div>
  </div>
</footer>

<div class="abs copyright">Copright@lumopharma 2020 All&nbsp; Right Reserved</div>

</body>
</html>
```